Town Planning business needs a design (template) for planning reports and letters

I'm looking to develop a report and a letter template. I prepare town planning reports in NSW, Australia. Fairly straight forward reports which would include figures and tables. I can provide examples of similar reports. I have a logo design which I can also provide ( I have attached one file).

Target Market(s)

Professionals, local and state governments

Industry/Entity Type

Property Development

Requirements
Must have
• Title page, contents, 3 - 4 levels of headings, tables and ability to inset figures/photos and Annexure pages at end of report
Nice to have
• Ability to include short details of project in header or footer

```html
<!DOCTYPE html>
<html lang="en">
<head>
<meta charset="utf-8">
<title>Town Planning Report 2023 – Report and Letterhead Templates</title>
<link href="https://fonts.googleapis.com/css2?family=Jost:ital,wght@0,400;0,500;0,600;1,500&family=Montserrat:wght@700;800&display=swap" rel="stylesheet">
<style>
  :root {
    --backdrop: #666666;
    --paper: #ffffff;
    --cover-tint: #d8eefb;
    --brand-blue: #3db0ef;
    --ink: #22262b;
    --navy: #1d2b4f;
    --rule: #7d8a9c;
    --table-head: #d4e8fb;
  }
  * { margin: 0; padding: 0; box-sizing: border-box; }
  html, body { width: 712px; height: 1200px; overflow: hidden; }
  body { background: var(--backdrop); position: relative; font-family: "Jost", sans-serif; color: var(--ink); }

  .page-slot { position: absolute; width: 249px; height: 353px; }
  .page {
    position: absolute; left: 0; top: 0;
    width: 519px; height: 735px;
    background: var(--paper);
    transform: scale(0.48); transform-origin: 0 0;
    overflow: hidden;
  }
  .page--cover { background: var(--cover-tint); }

  .brand { position: absolute; left: 49px; top: 26px; display: flex; align-items: center; gap: 9px; }
  .brand__mark { width: 36px; height: 36px; background: var(--brand-blue); }
  .brand__name { font-family: "Jost", sans-serif; font-weight: 600; font-size: 20px; line-height: 22px; color: var(--ink); letter-spacing: 0.3px; }

  .cover-title { position: absolute; left: 101px; top: 284px; font-weight: 500; font-size: 32px; line-height: 38px; color: var(--ink); }

  .footer-band { position: absolute; left: 0; top: 679px; width: 519px; height: 37px; }
  .footer-band svg { position: absolute; inset: 0; }
  .footer-band__title { position: absolute; right: 79px; top: 11px; font-size: 11.5px; color: #fff; letter-spacing: 0.2px; }
  .footer-band__divider { position: absolute; left: 452px; top: 0; width: 1.5px; height: 37px; background: var(--brand-blue); }
  .footer-band__number { position: absolute; left: 467px; top: 11px; font-size: 11.5px; color: #fff; }

  .section-heading { position: absolute; left: 49px; font-family: "Montserrat", sans-serif; font-weight: 800; font-size: 14.5px; color: var(--brand-blue); letter-spacing: 0.3px; }
  .body-copy { position: absolute; left: 49px; width: 421px; font-size: 9px; line-height: 12.7px; text-align: justify; }
  .body-copy p + p { margin-top: 12.7px; }

  .contents { position: absolute; left: 105px; top: 195px; width: 265px; }
  .contents__heading { font-family: "Montserrat", sans-serif; font-weight: 800; font-size: 14.5px; color: var(--brand-blue); margin-bottom: 22px; }
  .contents__list { list-style: none; }
  .contents__item { display: flex; justify-content: space-between; font-size: 8px; height: 31.4px; }

  .table-label { position: absolute; left: 49px; font-family: "Montserrat", sans-serif; font-weight: 700; font-size: 7.5px; color: var(--navy); }
  .fee-table { position: absolute; left: 49px; width: 421px; border-collapse: collapse; font-size: 7.2px; color: var(--ink); }
  .fee-table th, .fee-table td { border: 0.8px solid var(--rule); padding: 4px 4px; vertical-align: top; }
  .fee-table th { background: var(--table-head); font-weight: 400; color: var(--navy); text-align: left; height: 21px; vertical-align: middle; }
  .fee-table--product th { text-align: center; font-weight: 600; }
  .fee-table .item { font-weight: 500; }
  .fee-table .amount { text-align: right; }
  .fee-table .desc { padding-left: 5px; line-height: 10px; }

  .caption { position: absolute; left: 454px; top: 1158px; font-family: "Jost", sans-serif; font-style: italic; font-weight: 500; font-size: 15px; color: #fff; }
</style>
</head>
<body>

<!-- Cover -->
<div class="page-slot" style="left:370px; top:53px;">
  <section class="page page--cover">
    <div class="brand"><span class="brand__mark"></span><span class="brand__name">FIELDSTONE<br>PLANNING</span></div>
    <h1 class="cover-title">TOWN PLANNING<br>REPORT 2023</h1>
    <div class="footer-band">
      <svg width="519" height="37" viewBox="0 0 519 37"><rect width="519" height="37" fill="var(--brand-blue)"/><path d="M255 0 L519 0 L519 37 L190 37 Q225 22 255 0 Z" fill="var(--ink)"/></svg>
      <span class="footer-band__title">TOWN PLANNING REPORT 2023</span><span class="footer-band__divider"></span><span class="footer-band__number">1</span>
    </div>
  </section>
</div>

<!-- Contents -->
<div class="page-slot" style="left:93px; top:426px;">
  <section class="page">
    <div class="brand"><span class="brand__mark"></span><span class="brand__name">FIELDSTONE<br>PLANNING</span></div>
    <nav class="contents">
      <h2 class="contents__heading">CONTENTS</h2>
      <ul class="contents__list">
        <li class="contents__item"><span>About Us</span><span>3</span></li>
        <li class="contents__item"><span>Your FSP Team</span><span>4</span></li>
        <li class="contents__item"><span>Duty of Care</span><span>5</span></li>
        <li class="contents__item"><span>Recommencement of Travel</span><span>6</span></li>
        <li class="contents__item"><span>Unused Tickets and Refunds</span><span>7</span></li>
        <li class="contents__item"><span>Monitoring Client Expectations</span><span>8</span></li>
        <li class="contents__item"><span>Self-Booking Tools and Technology</span><span>9</span></li>
        <li class="contents__item"><span>Field Notes</span><span>10</span></li>
        <li class="contents__item"><span>nagement Fees</span><span>21</span></li>
      </ul>
    </nav>
    <div class="footer-band">
      <svg width="519" height="37" viewBox="0 0 519 37"><rect width="519" height="37" fill="var(--brand-blue)"/><path d="M205 0 L519 0 L519 37 L140 37 Q175 20 205 0 Z" fill="var(--ink)"/></svg>
      <span class="footer-band__title">TOWN PLANNING REPORT 2023</span><span class="footer-band__divider"></span><span class="footer-band__number">2</span>
    </div>
  </section>
</div>

<!-- Body page -->
<div class="page-slot" style="left:370px; top:426px;">
  <section class="page">
    <div class="brand"><span class="brand__mark"></span><span class="brand__name">FIELDSTONE<br>PLANNING</span></div>
    <h2 class="section-heading" style="top:110px;">SUBTTLE&nbsp; 01 LOREM&nbsp; IPSUM</h2>
    <div class="body-copy" style="top:136px;">
      <p>Lorem ipsum dolor sit amet, consectetur adipiscing elit. Sed a augue auctor, condimentum velit id, efficitur sem. In ac leo vitae ante rhoncus porttitor vitae at velit. Ut a ligula at ante pulvinar vestibulum a at ex. Ut finibus nulla sed sem lacinia, nec venenatis ligula fermentum. Cras in mauris dignissim odio varius pharetra at non erat. Curabitur ac risus ipsum. Vestibulum nunc tellus, vulputate molestie auctor nec, auctor nec arcu. Vivamus rutrum bibendum orci. Aenean ullamcorper sem sem, vel placerat ipsum tempor sit amet. Pellentesque molestie fermentum urna vel molestie. Etiam pellentesque tincidunt aliquam. Maecenas sit amet pellentesque odio. Vivamus hendrerit eros non tincidunt ornare. Sed mattis blandit diam sit amet condimentum. Quisque vel mattis mi. Aliquam id ornare dui, quis bibendum ipsum.</p>
      <p>Integer sagittis felis eget interdum rutrum. Vestibulum ante ipsum primis in faucibus orci luctus et ultrices posuere cubilia curae; Nam vulputate ante mollis risus mattis scelerisque. Cras elementum est justo, et tempus purus dapibus id. Sed porttitor ipsum at ipsum gravida volutpat. Fusce tincidunt bibendum libero tempus molestie. Pellentesque habitant morbi tristique senectus et netus et malesuada fames ac turpis egestas. Praesent ac bibendum lectus. Aliquam imperdiet nulla arcu, at ornare lectus eleifend rhoncus. In faucibus, orci eu faucibus placerat, diam magna vestibulum augue, sit amet aliquam lorem tellus et mauris.</p>
      <p>Aenean finibus, est ac dignissim laoreet, libero mauris aliquam arcu, ac suscipit erat tortor feugiat lacus. Praesent et dui sed magna consectetur consequat. Fusce a tempus arcu. In auctor neque massa, ut porttitor tellus gravida sed. Vivamus quis quam est. Interdum et malesuada fames ac ante ipsum primis in faucibus. Sed vel mollis massa. Vivamus sagittis, metus convallis molestie facilisis, arcu est eleifend urna, rhoncus ullamcorper augue sem at lacus. Sed quis vulputate sapien, nec cursus justo. Fusce pretium commodo lorem, quis finibus enim fringilla sit amet. Suspendisse vehicula, odio quis tincidunt feugiat, lectus mauris ultricies arcu, vel hendrerit mi massa nec nibh. Quisque pharetra elit id felis facilisis dapibus. Aenean sit amet mi egestas, lacinia justo eget, pellentesque quam. Nam sodales mauris non aliquam mollis.</p>
      <p>Maecenas nisl ante, consectetur eu suscipit vel, condimentum ac tortor. Quisque gravida metus velit, vitae sodales nulla varius vitae. Class aptent taciti sociosqu ad litora torquent per conubia nostra, per inceptos himenaeos. Class aptent taciti sociosqu ad litora torquent per conubia nostra, per inceptos himenaeos. Duis risus magna, posuere id dui in, auctor dictum erat. Suspendisse et tempor sem. Vivamus id eleifend leo. Donec sit amet eros tellus.</p>
      <p>Mauris eu justo ut est iaculis rutrum. Nam quam ante, congue et justo sit amet, ultrices ullamcorper elit. Vestibulum ante ipsum primis in faucibus orci luctus et ultrices posuere cubilia curae; Nam mattis augue ac lectus scelerisque, ut euismod tellus tincidunt. Donec semper, dui maximus eleifend ornare, augue erat lacinia nibh, a varius mi leo nec velit. Mauris vulputate, metus non gravida faucibus, velit lectus ornare tellus, ac scelerisque sem metus vel sapien. Sed quis suscipit libero. Proin pharetra massa eu nisi ros eget, feugiat fringilla dolor.</p>
    </div>
    <div class="footer-band">
      <svg width="519" height="37" viewBox="0 0 519 37"><rect width="519" height="37" fill="var(--brand-blue)"/><path d="M205 0 L519 0 L519 37 L140 37 Q175 20 205 0 Z" fill="var(--ink)"/></svg>
      <span class="footer-band__title">TOWN PLANNING REPORT 2023</span><span class="footer-band__divider"></span><span class="footer-band__number">3</span>
    </div>
  </section>
</div>

<!-- Tables page -->
<div class="page-slot" style="left:93px; top:796px;">
  <section class="page">
    <div class="brand"><span class="brand__mark"></span><span class="brand__name">FIELDSTONE<br>PLANNING</span></div>
    <h2 class="section-heading" style="top:110px;">SUBTTLE&nbsp; 02 LOREM&nbsp; IPSUM</h2>
    <div class="body-copy" style="top:136px;">
      <p>Lorem ipsum dolor sit amet, consectetur adipiscing elit. Sed a augue auctor, condimentum velit id, efficitur sem. In ac leo vitae ante rhoncus porttitor vitae at velit. Ut a ligula at ante pulvinar vestibulum a at ex. Ut finibus nulla sed sem lacinia, nec venenatis ligula fermentum. Cras in mauris dignissim odio varius pharetra at non erat. Curabitur ac risus ipsum. Vestibulum nunc tellus, vulputate molestie auctor nec, auctor nec arcu. Vivamus rutrum bibendum orci. Aenean ullamcorper sem sem, vel placerat ipsum tempor sit amet. Pellentesque molestie fermentum urna vel molestie. Etiam pellentesque tincidunt aliquam..</p>
    </div>
    <div class="table-label" style="top:241px;">SERVICING FEES</div>
    <table class="fee-table" style="top:252px;">
      <colgroup><col style="width:29px"><col style="width:258px"><col style="width:54px"><col style="width:80px"></colgroup>
      <tr><th></th><th>Lorem Ipum</th><th>Lorem Ipum</th><th>Lorem Ipum</th></tr>
      <tr style="height:22px"><td>1</td><td class="item">Loremipsum dolor</td><td class="amount">$15</td><td class="amount">$15</td></tr>
      <tr style="height:22px"><td>2</td><td class="item">Loremipsum dolor</td><td class="amount">$12</td><td class="amount">$35</td></tr>
      <tr style="height:44px"><td>3</td><td class="item">Loremipsum dolor</td><td></td><td style="line-height:10px">Sydney<br>$50.00<br>Interstate&nbsp; $75.00</td></tr>
      <tr style="height:32px"><td>4</td><td class="item">Loremipsum dolor</td><td class="amount" style="line-height:10px">$50 per contract</td><td class="amount">$50 per contract</td></tr>
    </table>
    <div class="table-label" style="top:416px;">PRODUCT FEES</div>
    <table class="fee-table fee-table--product" style="top:426px;">
      <colgroup><col style="width:29px"><col style="width:258px"><col style="width:134px"></colgroup>
      <tr><th></th><th>Lorem Ipum</th><th>Lorem</th></tr>
      <tr style="height:48px"><td>1</td><td class="desc">Integer sagittis felis eget interdum rutrum. Vestibulum ante ipsum primis in faucibus orci luctus et ultrices posuere cubilia curae; Nam vulputate ante mollis risus mattis scelerisque.</td><td class="amount" style="line-height:16px; padding-top:10px">Included<br>$150 per hour</td></tr>
      <tr style="height:53px"><td>2</td><td class="desc">Integer sagittis felis eget interdum rutrum. Vestibulum ante ipsum primis in faucibus orci luctus et ultrices posuere cubilia curae; Nam vulputate ante mollis risus mattis scelerisque.</td><td class="amount" style="vertical-align:bottom">$600</td></tr>
      <tr style="height:44px"><td>3</td><td class="desc">Integer sagittis felis eget interdum rutrum. Vestibulum ante ipsum primis in faucibus orci luctus et ultrices posuere cubilia curae; Nam vulputate ante mollis risus mattis scelerisque.</td><td class="amount" style="vertical-align:middle">Included</td></tr>
      <tr style="height:43px"><td>4</td><td class="desc">Integer sagittis felis eget interdum rutrum. Vestibulum ante ipsum primis in faucibus orci luctus et ultrices posuere cubilia curae; Nam vulputate ante mollis risus mattis scelerisque.</td><td class="amount">Included</td></tr>
    </table>
    <div class="footer-band">
      <svg width="519" height="37" viewBox="0 0 519 37"><rect width="519" height="37" fill="var(--brand-blue)"/><path d="M205 0 L519 0 L519 37 L140 37 Q175 20 205 0 Z" fill="var(--ink)"/></svg>
      <span class="footer-band__title">TOWN PLANNING REPORT 2023</span><span class="footer-band__divider"></span><span class="footer-band__number">4</span>
    </div>
  </section>
</div>

<!-- Letterhead -->
<div class="page-slot" style="left:370px; top:796px;">
  <section class="page">
    <div class="brand"><span class="brand__mark"></span><span class="brand__name">FIELDSTONE<br>PLANNING</span></div>
    <div class="footer-band">
      <svg width="519" height="37" viewBox="0 0 519 37"><rect width="519" height="37" fill="var(--brand-blue)"/><path d="M205 0 L519 0 L519 37 L140 37 Q175 20 205 0 Z" fill="var(--ink)"/></svg>
      <span class="footer-band__title">TOWN PLANNING REPORT 2023</span><span class="footer-band__divider"></span><span class="footer-band__number">4</span>
    </div>
  </section>
</div>

<div class="caption">Letterhead</div>

</body>
</html>
```